Fitness website

Website for a fitness brand (see attached specs). Design needs to be modern and vibrant with CTAs on every page. We will provide logos, images, etc but for now user placeholder text and images. For now use the name 'Veltrano Athletics' as the name to use on the design. The goal of this site is to either get people to join the gym (5 physical locations across the US); buy an online program; buy merch or supplements or sign up for the newsletter. Pleas use images from this foldeR: https://files.quorbex.net/share/8kTq27wLmZr

We will be coding this in ReactNative. Lots more work for the winner as well, this is a 1st project for us.

Target Market(s)

fitness enthusiats

Industry/Entity Type

fitness, health, wellness

Number of Pages Required

5+ page

Font styles to use
Other font styles liked:
• Lato

Colors
0054AA
0677BA
7BADD7
CADEEF
E8F1F8
0094D4
00A9DD
6FCCEA
C7EBF8
E9F6FB
00AB8E
00BBA5
67D7C9
C6EFE9
E9F9F6
EE7325
F08F49
F5BC92
FAE3D3
FDF4ED

Requirements
Must have
• must be reactive. most people will view it first on mobile
Nice to have
• video in hero section of top of home page

```html
<!DOCTYPE html>
<html lang="en">
<head>
<meta charset="utf-8">
<title>Veltrano Athletics</title>
<link href="https://fonts.googleapis.com/css2?family=Russo+One&family=Poppins:wght@400;500;600;700&display=swap" rel="stylesheet">
<style>
:root{
  --green:#1a8b3d;
  --green-dark:#136b2e;
  --green-soft:#eaf7ee;
  --orange:#ee7325;
  --ink:#111;
  --gray:#555;
  --white:#fff;
  --black:#0b0b0b;
  --head:"Russo One",sans-serif;
  --body:"Poppins",sans-serif;
}
*{box-sizing:border-box;margin:0;padding:0}
html,body{width:1200px;height:4996px;overflow:hidden}
body{font-family:var(--body);color:var(--ink);background:var(--white);position:relative}
h1,h2,h3{font-family:var(--head);font-weight:400}
a{color:inherit;text-decoration:none}
.btn{display:inline-block;background:var(--orange);color:var(--white);font-size:13px;font-weight:500;padding:11px 20px;border-radius:6px;text-transform:uppercase;letter-spacing:.3px}

/* hero */
.hero{position:absolute;top:0;left:0;width:1200px;height:670px;background:radial-gradient(ellipse at 55% 60%,#5a4a3d 0%,#2b2623 45%,#141313 100%)}
.nav{position:absolute;top:22px;left:60px;right:60px;height:48px;display:flex;align-items:center}
.logo{font-family:var(--body);font-weight:700;color:var(--green);font-size:22px;letter-spacing:.5px}
.menu{display:flex;gap:34px;margin-left:150px;font-size:13px;color:var(--white)}
.menu .active{color:#2fbf5a}
.tools{margin-left:auto;display:flex;gap:18px;align-items:center}
.hero-copy{position:absolute;top:172px;left:0;width:1200px;text-align:center;color:var(--white)}
.hero-copy h1{font-size:46px;line-height:62px;letter-spacing:.5px}
.hero-copy p{font-size:15px;line-height:26px;margin:22px auto 24px;width:560px}
.hero-copy .btn{padding:11px 18px}

/* ticker */
.ticker{position:absolute;top:630px;left:0;width:1200px;height:150px;overflow:hidden}
.band{position:absolute;left:-40px;width:1300px;height:40px;display:flex;align-items:center;gap:28px;white-space:nowrap;color:var(--white);font-weight:700;font-size:16px;padding-left:30px}
.band.one{top:48px;background:var(--green-dark);transform:rotate(-2deg)}
.band.two{top:50px;background:var(--green);transform:rotate(2.2deg)}
.band .dot{width:14px;height:14px;border:2.5px solid var(--white);border-radius:50%}

/* about */
.about{position:absolute;top:766px;left:0;width:1200px;height:480px;background:linear-gradient(90deg,#e9e6e2 0%,#f7f6f4 30%,#fbfbfa 50%,#f7f6f4 70%,#e6e3df 100%);text-align:center}
.about h2{font-size:38px;margin-top:36px}
.about p{font-size:12.5px;line-height:19.5px;color:var(--gray);width:650px;margin:14px auto 0}
.stats{display:flex;justify-content:center;margin-top:26px}
.stat{padding:0 28px;border-left:1px solid #cfd8cf}
.stat:first-child{border-left:0}
.stat b{display:block;font-size:28px;color:var(--green);font-weight:600;line-height:32px}
.stat span{font-size:11.5px;color:var(--green)}
.about .btn{margin-top:26px}

/* train */
.train{position:absolute;top:1245px;left:0;width:1200px;height:710px;background:var(--green);color:var(--white)}
.train-photo{position:absolute;left:60px;top:76px;width:489px;height:560px;border-radius:16px;background:linear-gradient(160deg,#3c4a66,#1c2236 60%,#2d2a2a)}
.train-body{position:absolute;left:637px;top:68px;width:503px}
.train-body h2{font-size:36px}
.train-body>p{font-size:14px;line-height:24px;margin-top:8px}
.feature{display:flex;gap:28px;padding:24px 0 22px;border-bottom:1px solid rgba(255,255,255,.3)}
.feature:last-child{border-bottom:0}
.feature svg{flex:0 0 54px}
.feature h3{font-family:var(--body);font-weight:600;font-size:17px}
.feature p{font-size:12px;line-height:20px;margin-top:4px}

/* testimonials */
.clients{position:absolute;top:1955px;left:0;width:1200px;height:493px;text-align:center}
.clients h2{font-size:36px;margin-top:72px}
.cards{position:absolute;top:180px;left:60px;display:flex;gap:15px}
.quote{position:relative;width:352px;height:240px;border:2px solid var(--green);border-radius:14px;padding:58px 26px 0}
.quote.alt{border-color:var(--orange)}
.avatar{position:absolute;top:-38px;left:137px;width:76px;height:76px;border-radius:50%;border:3px solid var(--green);background:linear-gradient(#dcd6cf,#8a7a6c)}
.quote.alt .avatar{border-color:var(--orange)}
.quote p{font-size:12px;line-height:21px;color:var(--gray)}
.quote b{display:block;margin-top:16px;font-size:14px;font-weight:600}
.quote span{font-size:12px;color:var(--gray)}

/* join */
.join{position:absolute;top:2448px;left:0;width:1200px;height:431px;background:linear-gradient(90deg,#0c0c0c 0%,#141414 45%,#1e1e1e 55%)}
.join-photo{position:absolute;right:0;top:0;width:620px;height:431px;background:linear-gradient(100deg,rgba(20,20,20,1) 0%,#3a3b40 30%,#4a4645 60%,#25272c 100%)}
.join-body{position:absolute;left:60px;top:68px;color:var(--white);width:440px}
.join-body h2{font-size:38px;line-height:48px}
.join-body p{font-size:14px;line-height:24px;margin-top:10px}
.field{margin-top:24px;width:376px;height:40px;border:1px solid #666;border-radius:6px;background:rgba(255,255,255,.12);font-size:12px;padding:12px 16px}
.join-body .btn{margin-top:18px}

/* membership */
.membership{position:absolute;top:2879px;left:0;width:1200px;height:578px;text-align:center}
.membership h2{font-size:36px;margin-top:72px}
.plans{position:absolute;top:154px;left:174px;display:flex;gap:14px;align-items:center}
.plan{width:274px;height:344px;background:var(--green-soft);border-radius:16px;padding-top:40px}
.plan.featured{height:356px;background:var(--white);border:2px solid var(--orange);position:relative;padding-top:60px}
.badge{position:absolute;top:-2px;left:70px;width:130px;height:28px;background:var(--orange);color:var(--white);font-size:12px;line-height:28px;border-radius:0 0 12px 12px}
.plan h3{font-family:var(--body);font-weight:600;font-size:17px}
.price{font-size:29px;font-weight:700;color:var(--green);margin-top:14px;line-height:34px}
.per{font-size:12px;color:var(--green)}
.plan ul{list-style:none;text-align:left;margin:14px 0 0 44px;font-size:12px;color:var(--gray)}
.plan li{display:flex;gap:10px;align-items:center;height:27px}
.plan .btn{margin-top:20px;padding:10px 30px}

/* blog */
.blog{position:absolute;top:3457px;left:0;width:1200px;height:582px;background:var(--green);text-align:center}
.blog h2{font-size:36px;color:var(--white);margin-top:72px}
.posts{position:absolute;top:148px;left:60px;display:flex;gap:15px;text-align:left}
.post{width:351px;height:358px;background:var(--white);border-radius:12px;padding:10px;position:relative}
.post-photo{height:196px;border-radius:8px}
.post h3{font-family:var(--body);font-weight:600;font-size:17px;margin:28px 0 0 2px}
.post p{font-size:12px;line-height:21px;color:var(--gray);width:240px;margin:6px 0 0 2px}
.arrow{position:absolute;right:16px;bottom:20px;width:48px;height:32px;border-radius:16px;background:var(--orange);display:flex;align-items:center;justify-content:center}

/* location */
.location{position:absolute;top:4039px;left:0;width:1200px;height:617px;text-align:center}
.location h2{font-size:36px;margin-top:72px}
.contact{position:absolute;top:160px;left:60px;width:330px;height:390px;background:var(--white);box-shadow:0 4px 20px rgba(0,0,0,.08);text-align:left;padding:26px 20px}
.contact h3{font-family:var(--body);font-weight:600;font-size:15px}
.branch{display:flex;gap:14px;margin-top:18px;padding:18px 18px;border-radius:4px;width:280px}
.branch.active{background:var(--orange);color:var(--white);height:170px}
.branch.soft{background:var(--green-soft);height:120px;margin-top:14px}
.pin{flex:0 0 32px;height:32px;border-radius:50%;background:var(--green);display:flex;align-items:center;justify-content:center}
.branch.active .pin{background:var(--white)}
.branch b{font-weight:500;font-size:15px}
.branch p{font-size:12px;line-height:20px;margin-top:4px}
.branch .tel{margin-top:16px;display:flex;gap:14px;align-items:center;font-size:14px;margin-left:-46px}
.rail{position:absolute;left:320px;top:92px;width:4px;height:280px;background:var(--green)}
.rail i{position:absolute;top:40px;left:-4px;width:12px;height:12px;border:2px solid var(--orange);border-radius:50%;background:var(--white)}
.map{position:absolute;left:419px;top:151px;width:722px;height:392px;background:linear-gradient(135deg,#cfe8d6,#e3efe4 50%,#d6ead8)}

/* footer */
.footer{position:absolute;top:4656px;left:0;width:1200px;height:340px;background:var(--black);color:var(--white);text-align:center}
.footer .logo{position:absolute;top:40px;left:0;width:1200px;font-size:34px;line-height:44px}
.reach{position:absolute;top:131px;left:0;width:1200px;display:flex;justify-content:center;gap:60px;font-size:12.5px}
.reach div{display:flex;align-items:center;gap:12px}
.ic{width:32px;height:32px;border-radius:50%;background:var(--orange);display:flex;align-items:center;justify-content:center}
.rule{position:absolute;left:60px;width:1080px;height:1px;background:#2c2c2c}
.rule.r1{top:186px}
.rule.r2{top:244px}
.links{position:absolute;top:206px;left:0;width:1200px;display:flex;justify-content:center;font-size:12px;line-height:18px}
.links a{padding:0 22px;border-left:1px solid #777}
.links a:first-child{border-left:0}
.social{position:absolute;top:252px;left:0;width:1200px;display:flex;justify-content:center;gap:8px}
.social span{width:32px;height:32px;border:2px solid var(--orange);border-radius:50%}
.copy{position:absolute;top:302px;left:0;width:1200px;font-size:12px;line-height:18px}
</style>
</head>
<body>

<header class="hero">
  <div role="img" aria-label="Athlete gripping a loaded barbell in a dark gym" style="position:absolute;inset:0"></div>
  <nav class="nav">
    <a class="logo" href="#">Veltrano Athletics</a>
    <div class="menu">
      <a class="active" href="#">Home</a><a href="#">About Us</a><a href="#">Programs</a><a href="#">Shop</a><a href="#">Members</a><a href="#">Locations</a><a href="#">Blogs</a>
    </div>
    <div class="tools">
      <svg width="18" height="18" viewBox="0 0 24 24" fill="none" stroke="#fff" stroke-width="2"><circle cx="10" cy="10" r="7"/><path d="M15 15l6 6"/></svg>
      <svg width="18" height="18" viewBox="0 0 24 24" fill="none" stroke="#fff" stroke-width="2"><circle cx="12" cy="8" r="4"/><path d="M4 21c1-5 15-5 16 0"/></svg>
      <svg width="20" height="20" viewBox="0 0 24 24" fill="none" stroke="#fff" stroke-width="2"><path d="M2 3h3l3 12h11l2-8H7"/><circle cx="9" cy="20" r="1.5"/><circle cx="18" cy="20" r="1.5"/><circle cx="20" cy="4" r="4" fill="#ee7325" stroke="none"/></svg>
    </div>
  </nav>
  <div class="hero-copy">
    <h1>UNLEASH YOUR POTENTIAL WITH<br>VELTRANO ATHLETICS</h1>
    <p>Train with elite coaches, proven programs, and a global community that pushes you to be your best.</p>
    <a class="btn" href="#">Start your free trial</a>
  </div>
</header>

<div class="ticker" aria-hidden="true">
  <div class="band one"><span>Training</span><i class="dot"></i><span>Fitness Sports</span><i class="dot"></i><span>Training</span><i class="dot"></i><span>Fitness Sports</span><i class="dot"></i><span>Training</span><i class="dot"></i><span>Fitness Sports</span><i class="dot"></i><span>Training</span><i class="dot"></i><span>Fitness Sports</span><i class="dot"></i><span>Training</span></div>
  <div class="band two"><span>Training</span><i class="dot"></i><span>Fitness Sports</span><i class="dot"></i><span>Training</span><i class="dot"></i><span>Fitness Sports</span><i class="dot"></i><span>Training</span><i class="dot"></i><span>Fitness Sports</span><i class="dot"></i><span>Training</span><i class="dot"></i><span>Fitness Sports</span><i class="dot"></i><span>Training</span></div>
</div>

<section class="about" role="img" aria-label="Faded photos of athletes training, behind the about text">
  <h2>ABOUT US</h2>
  <p>Lorem Ipsum has been the industry's standard dummy text ever since the 1500s, when an unknown printer took a galley of type and scrambled it to make a type specimen book. It has survived not only five centuries, but also the leap into electronic typesetting, remaining essentially unchanged. It was popularised in the 1960s with the release of Letraset sheets containing Lorem Ipsum passages, and more recently.</p>
  <p>Lorem Ipsum has been the industry's standard dummy text ever since the 1500s, when an unknown printer took a galley of type and scrambled it to make a type specimen book. It has survived not only five centuries, but also the leap into electronic typesetting, remaining essentially unchanged.</p>
  <div class="stats">
    <div class="stat"><b>140+</b><span>Expert Coachs</span></div>
    <div class="stat"><b>978+</b><span>Members joines</span></div>
    <div class="stat"><b>50+</b><span>Fitness Programs</span></div>
  </div>
  <a class="btn" href="#">Get started now</a>
</section>

<section class="train">
  <div class="train-photo" role="img" aria-label="Athlete lifting a barbell overhead"></div>
  <div class="train-body">
    <h2>TRAIN YOUR WAY</h2>
    <p>Lorem Ipsum has been the industry's standard dummy text ever since the 1500s, when an unknown.</p>
    <div class="feature">
      <svg width="54" height="54" viewBox="0 0 54 54" fill="none" stroke="#fff" stroke-width="2"><path d="M6 14h42M10 8v12M44 8v12"/><circle cx="27" cy="24" r="5"/><path d="M18 48l5-14h8l5 14M27 29v10"/></svg>
      <div><h3>Functional Fitness</h3><p>Lorem Ipsum has been the industry's standard dummy text ever since the 1500s, when an unknown.</p></div>
    </div>
    <div class="feature">
      <svg width="54" height="54" viewBox="0 0 54 54" fill="none" stroke="#fff" stroke-width="2"><circle cx="30" cy="32" r="14"/><path d="M24 32l4 4 8-8M8 12h16M16 6v12"/></svg>
      <div><h3>Competitive</h3><p>Ipsum has been the industry's standard dummy text ever since the 1500s, when an unknown.</p></div>
    </div>
    <div class="feature">
      <svg width="54" height="54" viewBox="0 0 54 54" fill="none" stroke="#fff" stroke-width="2"><circle cx="27" cy="10" r="5"/><path d="M14 24l13-8 13 8M27 16v18l-8 14M27 34l8 14M8 22v6M46 22v6"/></svg>
      <div><h3>Masters</h3><p>Lorem Ipsum has been the industry's standard dummy text ever since the 1500s, when an unknown.</p></div>
    </div>
    <div class="feature">
      <svg width="54" height="54" viewBox="0 0 54 54" fill="none" stroke="#fff" stroke-width="2"><circle cx="22" cy="20" r="12"/><circle cx="22" cy="20" r="5"/><path d="M32 28l14 14M18 34l-4 14h16"/></svg>
      <div><h3>Specialty</h3><p>Lorem Ipsum has been the industry's standard dummy text ever since the 1500s, when an unknown.</p></div>
    </div>
  </div>
</section>

<section class="clients">
  <h2>WHAT OUR CLIENTS SAYS</h2>
  <div class="cards">
    <div class="quote"><div class="avatar" role="img" aria-label="Client portrait"></div><p>Lorem Ipsum has been the industry's standard dummy text ever since the 1500s, when an unknown printer took a galley of type and scrambled it to make a type specimen book. It has survived not only five centuries.</p><b>Client Name</b><span>fitness training</span></div>
    <div class="quote alt"><div class="avatar" role="img" aria-label="Client portrait"></div><p>Lorem Ipsum has been the industry's standard dummy text ever since the 1500s, when an unknown printer took a galley of type and scrambled it to make a type specimen book. It has survived not only five centuries.</p><b>Client Name</b><span>fitness training</span></div>
    <div class="quote"><div class="avatar" role="img" aria-label="Client portrait"></div><p>Lorem Ipsum has been the industry's standard dummy text ever since the 1500s, when an unknown printer took a galley of type and scrambled it to make a type specimen book. It has survived not only five centuries.</p><b>Client Name</b><span>fitness training</span></div>
  </div>
</section>

<section class="join">
  <div class="join-photo" role="img" aria-label="Man curling a barbell in a gym"></div>
  <div class="join-body">
    <h2>JOIN THE ULTRA<br>COMMUNITY</h2>
    <p>Lorem Ipsum has been the industry's standard dummy text ever since the 1500s, when an unknown.</p>
    <div class="field">Enter Email Address</div>
    <a class="btn" href="#">Get started now</a>
  </div>
</section>

<section class="membership">
  <h2>OUR MEMBERSHIP</h2>
  <div class="plans">
    <div class="plan"><h3>Beginner Plan</h3><div class="price">$30</div><div class="per">Monthly</div>
      <ul><li><svg width="12" height="12" viewBox="0 0 12 12"><path d="M1 6l3 3 7-7" stroke="#1a8b3d" stroke-width="2" fill="none"/></svg>Unlimited Club access</li><li><svg width="12" height="12" viewBox="0 0 12 12"><path d="M1 6l3 3 7-7" stroke="#1a8b3d" stroke-width="2" fill="none"/></svg>Groud attendance</li><li><svg width="12" height="12" viewBox="0 0 12 12"><path d="M1 6l3 3 7-7" stroke="#1a8b3d" stroke-width="2" fill="none"/></svg>Gym visits</li><li><svg width="12" height="12" viewBox="0 0 12 12"><path d="M1 6l3 3 7-7" stroke="#1a8b3d" stroke-width="2" fill="none"/></svg>Visits to the bath complex</li></ul>
      <a class="btn" href="#">Join now</a></div>
    <div class="plan featured"><div class="badge">Most Popular</div><h3>Premium Plan</h3><div class="price">$60</div><div class="per">Monthly</div>
      <ul><li><svg width="12" height="12" viewBox="0 0 12 12"><path d="M1 6l3 3 7-7" stroke="#1a8b3d" stroke-width="2" fill="none"/></svg>Unlimited Club access</li><li><svg width="12" height="12" viewBox="0 0 12 12"><path d="M1 6l3 3 7-7" stroke="#1a8b3d" stroke-width="2" fill="none"/></svg>Groud attendance</li><li><svg width="12" height="12" viewBox="0 0 12 12"><path d="M1 6l3 3 7-7" stroke="#1a8b3d" stroke-width="2" fill="none"/></svg>Gym visits</li><li><svg width="12" height="12" viewBox="0 0 12 12"><path d="M1 6l3 3 7-7" stroke="#1a8b3d" stroke-width="2" fill="none"/></svg>Visits to the bath complex</li></ul>
      <a class="btn" href="#">Join now</a></div>
    <div class="plan"><h3>Ultimate Plan</h3><div class="price">$80</div><div class="per">Monthly</div>
      <ul><li><svg width="12" height="12" viewBox="0 0 12 12"><path d="M1 6l3 3 7-7" stroke="#1a8b3d" stroke-width="2" fill="none"/></svg>Unlimited Club access</li><li><svg width="12" height="12" viewBox="0 0 12 12"><path d="M1 6l3 3 7-7" stroke="#1a8b3d" stroke-width="2" fill="none"/></svg>Groud attendance</li><li><svg width="12" height="12" viewBox="0 0 12 12"><path d="M1 6l3 3 7-7" stroke="#1a8b3d" stroke-width="2" fill="none"/></svg>Gym visits</li><li><svg width="12" height="12" viewBox="0 0 12 12"><path d="M1 6l3 3 7-7" stroke="#1a8b3d" stroke-width="2" fill="none"/></svg>Visits to the bath complex</li></ul>
      <a class="btn" href="#">Join now</a></div>
  </div>
</section>

<section class="blog">
  <h2>LATEST BLOG POSTS</h2>
  <div class="posts">
    <article class="post"><div class="post-photo" role="img" aria-label="Woman training on a cable machine" style="background:linear-gradient(150deg,#2a2c34,#5a4c48)"></div><h3>Lorem Ipsum Has</h3><p>Lorem Ipsum has been the industry's standard dummy text ever since the 1500s, when an unknown printer took a galley.</p><span class="arrow"><svg width="18" height="14" viewBox="0 0 18 14" fill="none" stroke="#fff" stroke-width="2.5"><path d="M1 7h15M10 1l6 6-6 6"/></svg></span></article>
    <article class="post"><div class="post-photo" role="img" aria-label="Man lifting kettlebells in a gym" style="background:linear-gradient(150deg,#3b3d42,#6b6561)"></div><h3>Lorem Ipsum Has</h3><p>Lorem Ipsum has been the industry's standard dummy text ever since the 1500s, when an unknown printer took a galley.</p><span class="arrow"><svg width="18" height="14" viewBox="0 0 18 14" fill="none" stroke="#fff" stroke-width="2.5"><path d="M1 7h15M10 1l6 6-6 6"/></svg></span></article>
    <article class="post"><div class="post-photo" role="img" aria-label="Athlete working with battle ropes" style="background:linear-gradient(150deg,#8a8780,#2c2b2b)"></div><h3>Lorem Ipsum Has</h3><p>Lorem Ipsum has been the industry's standard dummy text ever since the 1500s, when an unknown printer took a galley.</p><span class="arrow"><svg width="18" height="14" viewBox="0 0 18 14" fill="none" stroke="#fff" stroke-width="2.5"><path d="M1 7h15M10 1l6 6-6 6"/></svg></span></article>
  </div>
</section>

<section class="location">
  <h2>VELTRANO LOCATION</h2>
  <div class="contact">
    <h3>GYM AREAS CONTACT</h3>
    <div class="branch active"><span class="pin"><svg width="14" height="16" viewBox="0 0 14 16"><path d="M7 1a5 5 0 0 1 5 5c0 4-5 9-5 9S2 10 2 6a5 5 0 0 1 5-5z" fill="#1a8b3d"/><circle cx="7" cy="6" r="2" fill="#fff"/></svg></span>
      <div><b>Veltrano</b><p>Lorem ipsum has been the industry's standard dummy text</p>
      <div class="tel"><span class="pin"><svg width="14" height="14" viewBox="0 0 24 24"><path d="M5 2h4l2 5-3 2a12 12 0 0 0 7 7l2-3 5 2v4a2 2 0 0 1-2 2A19 19 0 0 1 3 4a2 2 0 0 1 2-2z" fill="#1a8b3d"/></svg></span>+ 0198 555 0142</div></div></div>
    <div class="branch soft"><span class="pin"><svg width="14" height="16" viewBox="0 0 14 16"><path d="M7 1a5 5 0 0 1 5 5c0 4-5 9-5 9S2 10 2 6a5 5 0 0 1 5-5z" fill="#fff"/><circle cx="7" cy="6" r="2" fill="#1a8b3d"/></svg></span>
      <div><b>Veltrano</b><p style="color:#555">Lorem ipsum has been the industry's standard dummy</p></div></div>
    <div class="rail"><i></i></div>
  </div>
  <div class="map" role="img" aria-label="Map of the central United States showing gym locations"></div>
</section>

<footer class="footer">
  <span class="logo">Veltrano Athletics</span>
  <div class="reach">
    <div><span class="ic"><svg width="14" height="14" viewBox="0 0 24 24"><path d="M5 2h4l2 5-3 2a12 12 0 0 0 7 7l2-3 5 2v4a2 2 0 0 1-2 2A19 19 0 0 1 3 4a2 2 0 0 1 2-2z" fill="#fff"/></svg></span>+ 0198 555 0142</div>
    <div><span class="ic"><svg width="14" height="12" viewBox="0 0 14 12" fill="none" stroke="#fff" stroke-width="1.6"><rect x="1" y="1" width="12" height="10"/><path d="M1 1l6 5 6-5"/></svg></span>info@veltranoathletics.com</div>
    <div><span class="ic"><svg width="12" height="14" viewBox="0 0 14 16"><path d="M7 1a5 5 0 0 1 5 5c0 4-5 9-5 9S2 10 2 6a5 5 0 0 1 5-5z" fill="#fff"/></svg></span>Veltrano Athletics...</div>
  </div>
  <div class="rule r1"></div>
  <div class="links"><a href="#">Home</a><a href="#">About Us</a><a href="#">Program</a><a href="#">Shop</a><a href="#">Members</a><a href="#">Location</a><a href="#">Blogs</a></div>
  <div class="rule r2"></div>
  <div class="social"><span></span><span></span><span></span></div>
  <p class="copy">© 2025 Veltrano Athletics. All rights reserved.</p>
</footer>

</body>
</html>
```